HLD business cards Dr. Martin Voss

I need a business card designed for our dental office. We are a "general dental" practice.
Looking for a clean, professional but not too fancy design with our logo and contact information required.
front of card is information/standard business card, backside is appt reminder with lines for date and time of appt
doctors name: Dr. Martin Voss DMD
office name: Voss Family Dental
address: 4827 N Birchwell Ave Maple Shores, FL 33098
phone: 954-555-0173
Contact Information for Business Card
Office name, Doctor name, address, phone number...etc
- White/off white base color, blue and or black lettering

```html
<!DOCTYPE html>
<html lang="en">
<head>
<meta charset="utf-8">
<title>Voss Family Dental – Business Cards</title>
<link rel="stylesheet" href="https://fonts.googleapis.com/css2?family=Tinos:wght@400;700&family=Roboto:wght@300&display=swap">
<style>
  :root {
    --backdrop: #252d2d;
    --card: #ffffff;
    --brand-blue: #1a8ff0;
    --ink-gray: #8c8c8c;
    --rule-gray: #cfcfcf;
    --dot-gray: #b5b5b5;
  }
  * { margin: 0; padding: 0; box-sizing: border-box; }
  html, body { width: 1200px; height: 801px; overflow: hidden; background: var(--backdrop); }
  .stage {
    width: 1200px; height: 801px;
    display: flex; align-items: center; justify-content: center; gap: 40px;
  }
  .card {
    position: relative;
    width: 520px; height: 297px;
    background: var(--card);
    border-radius: 28px;
    box-shadow: 0 18px 40px rgba(0,0,0,.35);
    font-family: "Tinos", serif;
  }

  /* Front side */
  .brand-block {
    position: absolute; left: 30px; top: 0; width: 170px; height: 100%;
    display: flex; flex-direction: column; align-items: center; justify-content: center; gap: 12px;
  }
  .brand-dot { width: 30px; height: 30px; border-radius: 50%; background: var(--rule-gray); }
  .brand-name {
    color: var(--ink-gray); font-size: 20px; font-weight: 400;
    text-align: center; line-height: 1.25;
  }
  .divider {
    position: absolute; left: 220px; top: 58px; bottom: 58px;
    width: 1px; background: var(--rule-gray);
  }
  .contact-block { position: absolute; left: 250px; top: 62px; right: 24px; }
  .doctor-name { color: var(--ink-gray); font-size: 26px; font-weight: 700; letter-spacing: .5px; }
  .doctor-title { color: var(--ink-gray); font-size: 14px; letter-spacing: 1px; margin: 2px 0 0 92px; }
  .contact-list { list-style: none; margin-top: 36px; }
  .contact-item {
    display: flex; align-items: flex-start; gap: 10px;
    color: var(--brand-blue); font-size: 15px; line-height: 1.3; margin-bottom: 8px;
  }
  .contact-icon { flex: none; width: 18px; height: 18px; margin-top: 1px; }

  /* Back side */
  .reminder-brand {
    position: absolute; left: 0; right: 0; top: 66px;
    display: flex; flex-direction: column; align-items: center; gap: 14px;
  }
  .reminder-brand .brand-dot { width: 40px; height: 40px; }
  .reminder-brand .brand-name { font-size: 26px; }
  .appointment-lines {
    position: absolute; left: 40px; right: 40px; bottom: 56px;
    display: flex; gap: 18px;
    font-family: "Roboto", sans-serif; font-weight: 300; font-size: 14px; color: var(--dot-gray);
  }
  .field { flex: 1; display: flex; align-items: flex-end; gap: 6px; }
  .field-line { flex: 1; border-bottom: 1px dotted var(--dot-gray); height: 12px; }
</style>
</head>
<body>
<main class="stage">

  <section class="card card-front" aria-label="Business card front">
    <div class="brand-block">
      <span class="brand-dot"></span>
      <p class="brand-name">Voss Family<br>Dental</p>
    </div>
    <div class="divider"></div>
    <div class="contact-block">
      <h1 class="doctor-name">Dr. Martin Voss</h1>
      <p class="doctor-title">DMD</p>
      <ul class="contact-list">
        <li class="contact-item">
          <svg class="contact-icon" viewBox="0 0 18 18" aria-hidden="true">
            <circle cx="9" cy="9" r="9" fill="var(--brand-blue)"/>
            <path d="M6 4.8c.4-.3.9-.2 1.1.2l.8 1.5c.2.4.1.8-.2 1l-.6.5c.5 1.1 1.3 1.9 2.4 2.4l.5-.6c.3-.3.7-.4 1-.2l1.5.8c.4.2.5.7.2 1.1l-.6.8c-.4.5-1.1.6-1.7.4-2.2-.9-3.9-2.6-4.8-4.8-.2-.6-.1-1.3.4-1.7z" fill="#fff"/>
          </svg>
          <span>954-555-0173</span>
        </li>
        <li class="contact-item">
          <svg class="contact-icon" viewBox="0 0 18 18" aria-hidden="true">
            <circle cx="9" cy="9" r="9" fill="var(--brand-blue)"/>
            <path d="M9 4.2 4.2 8.6h1.5v4.6h2.4v-2.8h1.8v2.8h2.4V8.6h1.5z" fill="#fff"/>
          </svg>
          <span>4827 N Birchwell Ave<br>Maple Shores, FL 33098</span>
        </li>
      </ul>
    </div>
  </section>

  <section class="card card-back" aria-label="Appointment reminder card back">
    <div class="reminder-brand">
      <span class="brand-dot"></span>
      <p class="brand-name">Voss Family Dental</p>
    </div>
    <div class="appointment-lines">
      <div class="field"><span>Date</span><span class="field-line"></span></div>
      <div class="field"><span>Time</span><span class="field-line"></span></div>
    </div>
  </section>

</main>
</body>
</html>
```